2015 Conference Header

I would like a header designed for our conference next year. It will be used on all of our event promotional material. The information and images that can be used are in the drop box file. I have also included examples of what we have used in the past.

https://www.filevaultly.example/sh/7k2p4x9q1m3nz8/QWErty834LmnoPzx5TuvBn2Ck?dl=0

Industry/Entity Type

Event

Requirements
Must have
• To give you all a little more idea on our branding colours and designs our business website is www.harbecklanefab.example

```html
<!DOCTYPE html>
<html lang="en">
<head>
<meta charset="utf-8">
<title>Spincast 2015 Letterhead</title>
<link rel="stylesheet" href="https://fonts.googleapis.com/css2?family=Archivo+Narrow:wght@700&display=swap">
<style>
  :root {
    --paper: #ffffff;
    --ink: #3b2a22;
    --panel: #dcd9d6;
    --sunset-top: #e8946a;
    --sunset-mid: #b55a3a;
    --sunset-low: #3a2219;
    --rule: #a8402f;
  }
  html, body {
    margin: 0;
    padding: 0;
    overflow: hidden;
    background: var(--paper);
  }
  .page {
    position: relative;
    width: 849px;
    height: 1200px;
    background: var(--paper);
    overflow: hidden;
    font-family: "Archivo Narrow", "Arial Narrow", sans-serif;
    font-weight: 700;
    color: var(--ink);
  }
  .header-banner {
    position: absolute;
    left: 28px;
    top: 25px;
    width: 787px;
    height: 170px;
    background: var(--panel);
  }
  .beach-photo {
    position: absolute;
    left: 0;
    top: 0;
    width: 440px;
    height: 170px;
    background: linear-gradient(180deg, var(--sunset-top) 0%, var(--sunset-mid) 45%, var(--sunset-low) 100%);
  }
  .event-title {
    position: absolute;
    right: 50px;
    top: 14px;
    margin: 0;
    font-size: 46px;
    line-height: 50px;
    font-weight: 700;
    white-space: nowrap;
  }
  .event-location {
    position: absolute;
    left: 445px;
    top: 74px;
    font-size: 34px;
    line-height: 36px;
    white-space: nowrap;
  }
  .event-dates {
    position: absolute;
    right: 50px;
    top: 126px;
    font-size: 16px;
    line-height: 18px;
    white-space: nowrap;
  }
  .event-web {
    position: absolute;
    right: 50px;
    top: 146px;
    font-size: 19px;
    line-height: 20px;
    white-space: nowrap;
  }
  .footer-rule {
    position: absolute;
    left: 0;
    top: 1142px;
    width: 842px;
    height: 0;
    border-top: 1.5px solid var(--rule);
  }
  .footer-name {
    position: absolute;
    left: 0;
    width: 849px;
    top: 1128px;
    text-align: center;
    font-size: 14px;
    line-height: 14px;
  }
</style>
</head>
<body>
  <div class="page">
    <header class="header-banner">
      <div class="beach-photo" role="img" aria-label="Silhouetted people walking along a beach at sunset beside a jetty"></div>
      <h1 class="event-title">SPINCAST 2015</h1>
      <div class="event-location">Adelaide, Australia</div>
      <div class="event-dates">21 – 23 June</div>
      <div class="event-web">www.spincastconference.example</div>
    </header>
    <div class="footer-name">SPINCAST 2015</div>
    <div class="footer-rule"></div>
  </div>
</body>
</html>
```